Driver License Monitoring Application Marketing Website

We need a new web design for our web application. The product is called "PermitPulse." We provide a driver license monitoring service to companies and local government bodies with driver fleets. Our current website is available at www.permitpulse-example.com.

I prefer a clean, single-page design with good SEO. Attached are some PDFs with data about the project.

Target Market(s)

Companies with driver fleets, local government.

Industry/Entity Type

Government

Coding

Coded - Design and coding required

Number of Pages Required

1 page

Colors
000000

Requirements
Must have
• Content from current www.permitpulse-example.com and attached PDFs.
Nice to have
• Prefer a simple Bootstrap or similar design for easy editing.
• Room for a simple video explanation of how the product works (we don't have an actual video yet)

```html
<!DOCTYPE html>
<html lang="en">
<head>
<meta charset="utf-8">
<title>PermitPulse – Florida Driver License Monitoring</title>
<link rel="stylesheet" href="https://fonts.googleapis.com/css2?family=Montserrat:wght@600;700;800&family=Open+Sans:wght@400;600;700&family=Kreon:wght@300;400;700&display=swap">
<style>
:root{
  --bg-dark:#1d1d1d;
  --bg-mid:#2a2a2a;
  --bg-band:#262626;
  --teal:#2cc3ae;
  --teal-dark:#1fa393;
  --white:#ffffff;
  --grey-light:#cfcfcf;
  --grey:#8a8a8a;
  --grey-dim:#6a6a6a;
  --line:#3a3a3a;
}
*{margin:0;padding:0;box-sizing:border-box}
html,body{width:1200px;height:2765px;overflow:hidden;background:var(--bg-dark)}
body{position:relative;font-family:"Open Sans",Arial,sans-serif;color:var(--white)}
.abs{position:absolute}

/* header */
.site-header{position:absolute;left:0;top:0;width:1200px;height:92px;background:var(--bg-dark)}
.brand{position:absolute;left:44px;top:28px;font-family:"Kreon",Georgia,serif;font-weight:700;font-size:28px;color:var(--white);letter-spacing:.5px}
.main-nav{position:absolute;right:42px;top:36px;display:flex;gap:27px;font-size:14px;font-weight:600;text-transform:uppercase}
.main-nav a{color:var(--white);text-decoration:none}
.main-nav a.active{color:var(--teal)}

/* hero */
.hero{position:absolute;left:0;top:92px;width:1200px;height:728px;
  background:radial-gradient(ellipse at 50% 20%,#5b5b5b 0%,#3a3a3a 45%,#1f1f1f 100%)}
.hero-title{position:absolute;left:0;top:80px;width:1200px;text-align:center;font-family:"Montserrat",Arial,sans-serif;font-weight:800;font-size:76px;line-height:74px;letter-spacing:3px;text-transform:uppercase}
.hero-sub{position:absolute;left:0;top:250px;width:1200px;text-align:center;font-family:"Kreon",Georgia,serif;font-size:20px;line-height:31px;text-transform:uppercase;color:#e8e8e8}
.hero-vehicle{position:absolute;left:396px;top:332px;width:406px;height:212px;
  background:linear-gradient(180deg,#777 0%,#4a4a4a 60%,#2c2c2c 100%);border-radius:6px}

.btn{position:absolute;width:205px;height:63px;background:var(--teal);border-radius:3px;box-shadow:0 3px 0 var(--teal-dark);text-align:center;color:var(--white)}
.btn .btn-main{display:block;padding-top:11px;font-family:"Montserrat",Arial,sans-serif;font-weight:700;font-size:19px;letter-spacing:1.5px;line-height:22px}
.btn .btn-note{display:block;font-size:14px;line-height:18px;letter-spacing:.5px}

.social-rail{position:absolute;right:0;top:170px;width:55px}
.social-rail span{display:block;height:53px;margin-bottom:2px;background:rgba(120,120,120,.55)}
.search-tab{position:absolute;right:0;top:599px;width:55px;height:53px;background:rgba(60,60,60,.85)}

/* tabs */
.tab-band{position:absolute;left:0;top:820px;width:1200px;height:135px;background:var(--bg-band);border-bottom:4px solid var(--teal)}
.tab{position:absolute;top:0;height:131px;line-height:131px;font-family:"Montserrat",Arial,sans-serif;font-weight:600;font-size:22px}
.tab.active{left:234px;width:190px;background:var(--teal);text-align:center}
.tab-pointer{position:absolute;left:322px;top:957px}

/* overview */
.overview-title{position:absolute;left:0;top:1008px;width:1200px;text-align:center;font-family:"Montserrat",Arial,sans-serif;font-weight:800;font-size:36px;letter-spacing:1px;text-transform:uppercase}
.overview-title em{font-style:normal;color:var(--grey)}
.banner{position:absolute;left:46px;top:1093px}
.lead{position:absolute;left:0;top:1436px;width:1200px;text-align:center;font-family:"Kreon",Georgia,serif;font-size:20px}
.body-copy{position:absolute;left:46px;top:1496px;width:1108px;text-align:center;font-family:"Kreon",Georgia,serif;font-weight:300;font-size:14.5px;line-height:28px;color:var(--grey)}
.body-copy b{color:var(--white);font-weight:700}

/* cards */
.cards{position:absolute;left:0;top:1686px;width:1200px;height:581px;background:var(--bg-mid)}
.card{position:absolute;top:57px;width:258px}
.card-photo{width:258px;height:258px;border-radius:8px}
.card-photo.highlight{border:3px solid var(--teal)}
.card-title{margin-top:32px;text-align:center;font-family:"Kreon",Georgia,serif;font-size:23px;color:var(--grey)}
.card-sub{margin-top:14px;text-align:center;font-family:"Kreon",Georgia,serif;font-style:italic;font-weight:300;font-size:15px;color:var(--grey-dim)}
.card .btn{left:27px;top:408px}

/* footer */
.site-footer{position:absolute;left:0;top:2267px;width:1200px;height:428px;background:var(--bg-dark)}
.foot-col{position:absolute;top:34px}
.foot-col h3{font-family:"Montserrat",Arial,sans-serif;font-weight:800;font-size:28px;letter-spacing:.5px;text-transform:uppercase;margin-bottom:30px}
.address{font-size:12px;line-height:26.5px;color:var(--grey-light)}
.quick-links{list-style:none;width:255px}
.quick-links li{font-size:12.5px;color:var(--grey);height:38.5px;line-height:36px;border-bottom:1px solid var(--line)}
.quick-links li::before{content:"\203A  ";color:var(--grey)}
.quick-links li:first-child{color:var(--white)}
.tweet{width:245px;font-family:"Kreon",Georgia,serif;font-size:13px;line-height:24px;color:var(--grey);margin-bottom:18px}
.tweet b{color:var(--white);font-weight:700;font-family:"Open Sans",Arial,sans-serif;font-size:12px}
.field{width:255px;height:42px;margin-bottom:6px;background:#232323;font-size:13px;color:var(--grey-light);padding:11px 16px}
.field.tall{height:86px}
.submit{margin-top:12px;width:150px;height:38px;background:var(--teal);border-radius:2px;text-align:center;line-height:38px;font-family:"Montserrat",Arial,sans-serif;font-weight:700;font-size:14px;letter-spacing:2px}

.bottom-bar{position:absolute;left:0;top:2695px;width:1200px;height:70px;background:var(--bg-dark);border-top:1px solid var(--line)}
.copyright{position:absolute;left:44px;top:24px;font-size:13px;color:var(--grey)}
</style>
</head>
<body>

<header class="site-header">
  <div class="brand">PermitPulse</div>
  <nav class="main-nav">
    <a class="active" href="#">Home</a>
    <a href="#">License Monitoring</a>
    <a href="#">About Us</a>
    <a href="#">Contact</a>
    <a href="#">Client Login</a>
  </nav>
</header>

<section class="hero">
  <h1 class="hero-title">Florida Driver<br>License Monitoring</h1>
  <p class="hero-sub">Monitor your fleet electronically. Get alerts by email and online. Never let<br>another unlicensed or unauthorized driver behind the wheel.</p>
  <div class="hero-vehicle" role="img" aria-label="Black and white photo of a fleet garbage truck"></div>
  <a class="btn" style="left:498px;top:581px"><span class="btn-main">MORE INFO</span><span class="btn-note">track your fleet</span></a>
  <div class="social-rail"><span></span><span></span><span></span><span></span><span></span><span></span></div>
  <div class="search-tab">
    <svg width="55" height="53" viewBox="0 0 55 53"><circle cx="25" cy="24" r="7" fill="none" stroke="#fff" stroke-width="2.5"/><line x1="30" y1="29" x2="35" y2="34" stroke="#fff" stroke-width="3" stroke-linecap="round"/></svg>
  </div>
</section>

<nav class="tab-band">
  <div class="tab active">What We Do</div>
  <div class="tab" style="left:456px">Commercial</div>
  <div class="tab" style="left:648px">Government</div>
  <div class="tab" style="left:851px">About Us</div>
</nav>
<svg class="tab-pointer" width="24" height="13" viewBox="0 0 24 13"><polygon points="0,0 24,0 12,13" fill="#2cc3ae"/></svg>

<h2 class="overview-title">Track your <em>fleet for safety</em> and performance</h2>
<svg class="banner" width="1106" height="302" viewBox="0 0 1106 302" role="img" aria-label="Black and white photo of a silver car speeding on a curved road">
  <defs><linearGradient id="banner-tone" x1="0" y1="0" x2="1" y2="1"><stop offset="0" stop-color="#9a9a9a"/><stop offset=".5" stop-color="#e0e0e0"/><stop offset="1" stop-color="#6a6a6a"/></linearGradient></defs>
  <polygon points="0,0 1076,0 1106,151 1076,302 0,302 30,151" fill="url(#banner-tone)"/>
</svg>
<p class="lead">Monitor your drivers electronically, twenty-four hours a day.</p>
<p class="body-copy">How many of your drivers currently have a suspended license?&nbsp; The answer may surprise you.&nbsp; Driving with a suspended license is the most commonly committed offense in America. In 2011, over <b>1.8 million</b> licenses got suspended in Florida. With just over <b>15 million</b> drivers, that's <b>12%</b> of all licensed Florida drivers.</p>
<a class="btn" style="left:498px;top:1592px"><span class="btn-main">MORE INFO</span><span class="btn-note">track your fleet</span></a>

<section class="cards">
  <div class="card" style="left:42px">
    <div class="card-photo" role="img" aria-label="Photo of a businesswoman reading a tablet" style="background:linear-gradient(160deg,#d8d8d8,#7a7a7a)"></div>
    <div class="card-title">What We Do</div><div class="card-sub">License Monitoring</div>
    <a class="btn"><span class="btn-main">MORE INFO</span><span class="btn-note">track your fleet</span></a>
  </div>
  <div class="card" style="left:328px">
    <div class="card-photo highlight" role="img" aria-label="Dark photo of a truck front on the road" style="background:linear-gradient(180deg,#3a3a3a,#151515)"></div>
    <div class="card-title">Commercial</div><div class="card-sub">Private Sector</div>
    <a class="btn"><span class="btn-main">MORE INFO</span><span class="btn-note">track your fleet</span></a>
  </div>
  <div class="card" style="left:612px">
    <div class="card-photo" role="img" aria-label="Photo of a domed government capitol building" style="background:linear-gradient(180deg,#5a5a5a,#d4d4d4)"></div>
    <div class="card-title">Government</div><div class="card-sub">Public Sector</div>
    <a class="btn"><span class="btn-main">MORE INFO</span><span class="btn-note">track your fleet</span></a>
  </div>
  <div class="card" style="left:898px">
    <div class="card-photo" role="img" aria-label="Photo of a row of parked cars" style="background:linear-gradient(135deg,#b8b8b8,#3e3e3e)"></div>
    <div class="card-title">About Us</div><div class="card-sub">Florida Law Authorities</div>
    <a class="btn"><span class="btn-main">MORE INFO</span><span class="btn-note">track your fleet</span></a>
  </div>
</section>

<footer class="site-footer">
  <div class="foot-col" style="left:42px">
    <h3>Contact</h3>
    <p class="address">Northgate Fleet Records Ltd.<br><br>(Eastport Office / Head Office)<br>Level 4, Suite 402 / 18 Harbour Lane,<br>Eastport, VIC 3990<br>Phone: (03) 5550 0142<br>(Westvale Office)<br>Shop 2/41 Ridge Road,<br>Westvale QLD 4999<br>(07) 5550 0187</p>
  </div>
  <div class="foot-col" style="left:330px">
    <h3>Quick Links</h3>
    <ul class="quick-links">
      <li>Fleet overview</li><li>Alert settings</li><li>Driver records</li><li>Compliance reports</li><li>Pricing plans</li><li>Support center</li><li>Privacy policy</li>
    </ul>
  </div>
  <div class="foot-col" style="left:612px">
    <h3>Latest Tweets</h3>
    <p class="tweet"><b>@permitpulse</b> New alert rules now live for fleet managers across Florida, check your dashboard.<br>1 day ago</p>
    <p class="tweet"><b>@permitpulse</b> Quarterly license suspension report is ready for every county partner to download today.<br>1 day ago</p>
  </div>
  <div class="foot-col" style="left:903px">
    <h3>Contact Us</h3>
    <div class="field">Full Name</div>
    <div class="field">Email Address</div>
    <div class="field">Subject</div>
    <div class="field tall">Message</div>
    <div class="submit">SUBMIT</div>
  </div>
</footer>
<div class="bottom-bar"><p class="copyright">Copyright © 2015 PermitPulse - All Rights Reserved</p></div>

</body>
</html>
```